Brenmoor Systems Website Revamp

We need a full website for the oil and gas sector to showcase our company and our technology/services we provide to larger corporations. We want our website represent innovation and identity.

Background:

We are a service based company that specializes in:

- well services, and
-permanent applications
**(Please be aware that these are two different aspects to the oil and gas sector, both of which we supply to our customers)

We provide a wide range of jet pump technologies to address under performing reservoirs or problematic well producing conditions. We have field operations currently in: Canada, Oman, and Australia with efforts currently underway to expand in other markets. Therefore are needing a website to help promote a better comprehension of what we do and how we can solve their well issues. We are looking for

1.) Identity;
2.) Emphasis on better comprehension of our services for our clients to relate to us as a solution to their needs;
3.) User friendly interface - but new and exciting in this digital age .

Some examples of websites we like:

http://quorvalinc.com/how-we-work/
http://www.tandrisystems.com/tandri-system/
https://mirelfield.com/

Videos of our technologies:

https://www.vidoquay.com/watch?v=Qm47TzxR2pa
https://www.vidoquay.com/watch?v=Lk8WnbeT5yc

Target Market(s)

Petroleum Industry Clients

Coding

Coded - Design and coding required

Number of Pages Required

5+ page

Colors

Designer to choose colors to be used in the design.

Requirements
Must have
• See Project Description, and feel free to contact us with any questions/inquiries!
Nice to have
• Our color scheme is generally 'blue', to depict jet pumps (our service). However, we are open to ideas and artistic interpretation. Grayscale/offset colors/highlight colors etc.

```html
<!DOCTYPE html>
<html lang="en">
<head>
<meta charset="utf-8">
<title>Oil Company — Premium Oil and Gas Sector co.</title>
<link rel="stylesheet" href="https://fonts.googleapis.com/css2?family=Montserrat:wght@500;600;700&family=Open+Sans:wght@400;600&family=Roboto:wght@500;700&display=swap">
<style>
:root{
  --ink:#111;
  --white:#fff;
  --muted:#a9a9a9;
  --soft:#7d7d7d;
  --rule:#e6e6e6;
  --green-dark:#2f5a2c;
  --green:#4a7a3e;
  --steel-dark:#25292e;
  --steel:#3b4a5a;
  --teal:#1f7e86;
  --slate:#3c4a58;
  --slate-light:#63707c;
  --footer:#262626;
  --page-bg:#ffffff;
}
*{margin:0;padding:0;box-sizing:border-box}
html,body{width:1200px;height:1200px;overflow:hidden;background:var(--page-bg)}
body{position:relative;font-family:"Open Sans",Arial,sans-serif;color:var(--ink)}
.page{position:absolute;left:337px;top:0;width:523px;height:1200px;background:var(--white);box-shadow:0 0 14px rgba(0,0,0,.18);overflow:hidden}
.abs{position:absolute}
.shapes{position:absolute;left:0;top:0}

.site-header{position:absolute;left:0;top:0;width:523px;height:33px;background:var(--white)}
.brand{position:absolute;left:67px;top:7px;font-family:Roboto,Arial,sans-serif;font-weight:700;font-size:10px;letter-spacing:.1px}
.brand-tag{position:absolute;left:67px;top:20px;font-size:4.2px;color:#444}
.nav{position:absolute;top:14px;left:308px;display:flex;gap:13px;font-family:Roboto,Arial,sans-serif;font-weight:500;font-size:4.2px;color:#333}

.hero-title{position:absolute;left:90px;top:84px;font-family:Montserrat,Arial,sans-serif;font-weight:600;font-size:35px;color:var(--white);line-height:1}
.hero-sub{position:absolute;left:90px;top:126px;font-size:5.6px;color:#e8e8e8}
.pill{position:absolute;background:#000;color:var(--white);font-family:Montserrat,Arial,sans-serif;font-weight:700;font-size:4.4px;border-radius:9px;display:flex;align-items:center;justify-content:center}

.feature{position:absolute;top:238px;width:100px;text-align:center}
.feature svg{display:block;margin:0 auto}
.feature h3{font-family:Montserrat,Arial,sans-serif;font-weight:500;font-size:6.6px;margin-top:9px}
.feature p{font-size:5.3px;color:#c4c4c4;line-height:8px;margin-top:3px}

.band-title{position:absolute;left:0;width:523px;top:370px;text-align:center;font-family:Montserrat,Arial,sans-serif;font-weight:600;font-size:24px;line-height:20px;color:var(--white)}

.h2{position:absolute;left:90px;font-family:Montserrat,Arial,sans-serif;font-weight:600;color:var(--ink)}
.services-title{top:497px;font-size:21.5px}
.label-rule{position:absolute;height:1px;background:#9a9a9a}
.label{position:absolute;font-size:4px;color:#444}
.list{position:absolute;top:540px;font-size:5.4px;color:#9a9a9a;line-height:10px;list-style:none}

.news-title{top:870px;font-size:25px;line-height:20px}
.post{position:absolute;left:184px;top:951px;width:236px;height:14px;border-bottom:1px solid var(--rule);font-size:4.4px;color:#333}
.post time{position:absolute;right:0;top:0;font-size:3.6px;color:#c8c8c8}

.cta-title{position:absolute;left:90px;top:1065px;font-family:Montserrat,Arial,sans-serif;font-weight:600;font-size:25px;color:var(--white)}
.cta-text{position:absolute;left:90px;top:1094px;width:230px;font-size:5.6px;line-height:8px;color:#e6e6e6}
.footer{position:absolute;left:0;top:1170px;width:523px;height:30px;background:var(--footer)}
</style>
</head>
<body>
<div class="page">

  <svg class="shapes" width="523" height="1200" viewBox="0 0 523 1200">
    <defs>
      <linearGradient id="heroFill" x1="0" y1="0" x2="1" y2="1">
        <stop offset="0" stop-color="var(--teal)"/>
        <stop offset=".35" stop-color="#8f9499"/>
        <stop offset=".55" stop-color="var(--steel-dark)"/>
        <stop offset="1" stop-color="#1d2c3d"/>
      </linearGradient>
      <linearGradient id="bandFill" x1="0" y1="0" x2="1" y2="0">
        <stop offset="0" stop-color="var(--green-dark)"/>
        <stop offset=".6" stop-color="var(--green)"/>
        <stop offset="1" stop-color="var(--green-dark)"/>
      </linearGradient>
      <linearGradient id="ctaFill" x1="0" y1="0" x2="1" y2="1">
        <stop offset="0" stop-color="var(--slate)"/>
        <stop offset=".5" stop-color="var(--slate-light)"/>
        <stop offset="1" stop-color="#2f3a45"/>
      </linearGradient>
    </defs>
    <polygon role="img" aria-label="Photo of downhole jet pump tool on a dark background" points="0,33 519,33 519,168 0,216" fill="url(#heroFill)"/>
    <polygon role="img" aria-label="Green leaf photo backdrop" points="0,366 519,319 519,416 0,466" fill="url(#bandFill)"/>
    <line x1="0" y1="538" x2="523" y2="538" stroke="var(--rule)" stroke-width=".6"/>
    <rect role="img" aria-label="Minimal white interior photo" x="73" y="615" width="187" height="109" fill="#eeeeec"/>
    <rect role="img" aria-label="Blue sofa in a bright room photo" x="260" y="615" width="186" height="109" fill="#e9ebec"/>
    <rect role="img" aria-label="Jet pump nozzle parts render" x="73" y="724" width="187" height="110" fill="#dcdde2"/>
    <rect role="img" aria-label="Oil production rate chart after system install" x="260" y="724" width="186" height="110" fill="#f3f6ee"/>
    <line x1="0" y1="1002" x2="523" y2="1002" stroke="var(--rule)" stroke-width=".6"/>
    <polygon role="img" aria-label="Dark grey living room photo" points="0,1052 519,1002 519,1170 0,1170" fill="url(#ctaFill)"/>
  </svg>

  <header class="site-header">
    <div class="brand">OIL COMPANY</div>
    <div class="brand-tag">Premium Oil and Gas Sector co.</div>
    <nav class="nav"><span>HOME</span><span>ABOUT US</span><span>BLOG</span><span>MEMBERSHIP</span><span>CONTACT US</span></nav>
  </header>

  <h1 class="hero-title">oil company</h1>
  <p class="hero-sub">A short Description about the business</p>
  <a class="pill" style="left:90px;top:144px;width:53px;height:16px">MORE ABOUT US</a>

  <div class="feature" style="left:89px">
    <svg width="20" height="24" viewBox="0 0 20 24" fill="none" stroke="#111" stroke-width="1"><path d="M10 1a7 7 0 0 0-4 12.7V17h8v-3.3A7 7 0 0 0 10 1z"/><path d="M7 19h6M7.5 21h5M8 7l2 3 2-3M10 10v7"/></svg>
    <h3>creative works</h3>
    <p>Short description regarding this feature of the company</p>
  </div>
  <div class="feature" style="left:209px">
    <svg width="20" height="24" viewBox="0 0 20 24" fill="none" stroke="#111" stroke-width="1"><rect x="4" y="1" width="12" height="22" rx="2"/><path d="M8 3h4"/></svg>
    <h3>fast support</h3>
    <p>Short description regarding this feature of the company</p>
  </div>
  <div class="feature" style="left:329px">
    <svg width="22" height="24" viewBox="0 0 22 24" fill="none" stroke="#111" stroke-width="1"><path d="M1 7h20v16H1z"/><path d="M7 9V5a4 4 0 0 1 8 0v4"/></svg>
    <h3>online ordering</h3>
    <p>Short description regarding this feature of the company</p>
  </div>

  <h2 class="band-title">what makes us uniq<br>a bold feature.</h2>

  <h2 class="h2 services-title">what servecies do we offer?</h2>
  <div class="label-rule" style="left:54px;top:546px;width:33px"></div>
  <div class="label" style="left:93px;top:539px">Our Services &amp; Works</div>
  <ul class="list" style="left:186px">
    <li>1. Oil Service title</li><li>2. Oil Service title 2</li><li>3. Oil Service title 3</li><li>4. Oil Service title 4</li>
  </ul>
  <ul class="list" style="left:306px">
    <li>5. Technology Field</li><li>6. Technology Field 2</li><li>7. Technology Field 3</li><li>8. Technology Field 4</li>
  </ul>

  <h2 class="h2 news-title">latest news and articles<br>about company &amp; field</h2>
  <div class="label-rule" style="left:61px;top:953px;width:33px"></div>
  <div class="label" style="left:99px;top:947px">Our Blog</div>
  <article class="post">Hello world!<time>September 18, 2019</time></article>

  <h2 class="cta-title">ready to start?</h2>
  <p class="cta-text">A description about how the process of ordering works plus a direct link to order form and page to start order or be in touch</p>
  <a class="pill" style="left:90px;top:1120px;width:70px;height:16px">START YOUR PROJECT</a>

  <footer class="footer"></footer>
</div>
</body>
</html>
```